Tri-Fold Menu of Services for our Eyelash and Skin Care Spa

We need a beautiful spa service menu for our upscale spa in St. Charles Missouri. We specialize in providing treatments that are specific to the clients needs. Our services are eyelash extensions, skin care treatments, full body waxing and makeup application. Our spa colors are dark purples and greys and we are not opposed to additional colors that would complement those colors. We do a lot of eyelash extensions and while we do what those services listed we would like the skin care treatments to be in an area that would be noticed first. One of the attachments lists all of our services, descriptions and prices (please be sure to include all services and pricing. descriptions if possible). And our website has more information about us if needed. The website was not professionally done. So it DOESN'T represent our style exactly.

I HAVE ATTACHED A FEW PHOTOS BUT THEY DON'T HAVE TO BE USED.

Target Market(s)

women who would like to look their best, 35-55, annual income of 100,000+, she is usually busy and her children (if she has any) are high school age or older.

Industry/Entity Type

It Service

Font styles to use
Serif
Sans Serif

Requirements
Must have
• Must list all of our services. If it works to have the descriptions that would be great.
Nice to have
• If it works to have the descriptions of each service that would be great.

```html
<!DOCTYPE html>
<html lang="en">
<head>
<meta charset="utf-8">
<title>Lumen Lash &amp; Skin Spa – Service Menu</title>
<link href="https://fonts.googleapis.com/css2?family=Lato:wght@400;700;900&display=swap" rel="stylesheet">
<style>
:root{
  --ink:#28252d;
  --ink-deep:#1d1b21;
  --purple:#5e2ea0;
  --purple-bright:#7a45c9;
  --lilac:#8e63d6;
  --text:#f2f0f5;
  --muted:#b9b3c4;
  --paper:#ffffff;
  --stage:#e9e9e9;
}
*{margin:0;padding:0;box-sizing:border-box}
html,body{width:1200px;height:769px;overflow:hidden;background:var(--stage)}
body{font-family:"Lato",sans-serif;color:var(--text)}
.brochure{position:relative;width:1200px;height:769px;display:flex;background:var(--ink)}
.panel{position:relative;width:400px;height:769px;overflow:hidden}
.panel + .panel{border-left:1px solid rgba(0,0,0,.35)}
.decor{position:absolute;inset:0;width:100%;height:100%}
.photo{position:absolute}
/* menu panel */
.menu{position:absolute;left:26px;top:28px;width:350px;display:grid;grid-template-columns:1fr 1fr;column-gap:22px;row-gap:18px;font-size:11px}
.menu h2{font-size:13px;font-weight:900;letter-spacing:.04em;text-transform:uppercase;margin-bottom:4px}
.menu h3{font-size:11.5px;font-weight:900;margin:2px 0 3px}
.row{display:flex;justify-content:space-between;line-height:1.45}
.price{color:var(--lilac);font-weight:700}
.dot{display:inline-block;min-width:24px;padding:1px 4px;border-radius:9px;background:var(--purple);color:var(--text);font-size:8.5px;text-align:center;font-weight:700}
.note{color:var(--muted);font-size:8px;line-height:1.35;margin-top:4px}
.dur{color:var(--muted);font-size:9px}
.service{margin-bottom:6px}
.service strong{display:block;font-size:11px}
/* middle panel */
.addons{position:absolute;top:70px;left:0;width:400px;text-align:center}
.addons h2{font-size:26px;font-weight:900;margin-bottom:8px}
.addons .row{justify-content:center;gap:6px;font-size:11.5px;line-height:1.5}
.badge{position:absolute;left:130px;top:385px;width:140px;height:140px;border-radius:50%;background:radial-gradient(circle at 50% 40%,#3b3742,#1f1d23);box-shadow:0 6px 16px rgba(0,0,0,.5);display:flex;flex-direction:column;justify-content:center;align-items:center;text-align:center}
.badge .big{font-size:30px;font-weight:900;color:var(--lilac);line-height:1}
.badge .small{font-size:12px;font-weight:900;line-height:1.2;text-transform:uppercase}
.contact{position:absolute;left:0;top:575px;width:400px;text-align:center;font-size:12px;line-height:1.6}
.contact h2{color:var(--lilac);font-size:15px;font-weight:700;margin-bottom:2px}
.contact .lbl{color:var(--lilac)}
.social{display:flex;justify-content:center;gap:18px;margin-top:12px;font-size:11px;text-transform:uppercase}
.social span::before{content:"";display:inline-block;width:9px;height:9px;border-radius:50%;background:var(--purple-bright);margin-right:5px;vertical-align:-1px}
.social em{font-style:normal;color:var(--lilac)}
/* cover panel */
.brand{position:absolute;top:120px;left:0;width:400px;text-align:center}
.brand .name{font-size:46px;font-weight:400;color:var(--paper);letter-spacing:.02em}
.brand .tag{font-size:13px;font-weight:400;color:var(--paper);letter-spacing:.12em;margin-top:4px}
.call{position:absolute;left:62px;top:700px;padding:8px 20px;border-radius:8px;background:var(--ink-deep);font-size:17px;font-weight:900;letter-spacing:.02em}
.call .lbl{color:var(--lilac)}
</style>
</head>
<body>
<main class="brochure">

  <!-- Panel 1: service menu -->
  <section class="panel panel-menu">
    <svg class="decor" viewBox="0 0 400 769" aria-hidden="true">
      <path d="M0 560 C120 520 260 560 400 700 L400 769 L0 769Z" fill="var(--purple)"/>
      <path d="M0 590 C130 555 260 595 400 735 L400 769 L0 769Z" fill="var(--paper)"/>
    </svg>
    <div class="photo" role="img" aria-label="Photo of a client relaxing during a facial treatment" style="left:0;top:605px;width:400px;height:164px;background:linear-gradient(120deg,#f4e4da,#e3c2ad 55%,#f7f2ee);clip-path:path('M0 10 C130 -25 260 15 400 150 L400 164 L0 164Z')"></div>

    <div class="menu">
      <div>
        <h2>Eyelashes</h2>
        <h3>Classic</h3>
        <div class="row"><span>Full Set</span><span class="dot">175</span></div>
        <div class="row"><span>Demi Set</span><span class="dot">110</span></div>
        <div class="row"><span>Touch up</span><span class="dot">60</span></div>
      </div>
      <div>
        <h2>&nbsp;</h2>
        <h3>Volume Technique</h3>
        <div class="row"><span>Full Set</span><span class="dot">220</span></div>
        <div class="row"><span>Demi Set</span><span class="dot">135</span></div>
        <div class="row"><span>Touch up</span><span class="dot">72</span></div>
      </div>
      <div>
        <h2>Waxing</h2>
        <div class="row"><span>Eyebrows</span><span class="price">$17</span></div>
        <div class="row"><span>Upper Lip</span><span class="price">$14</span></div>
        <div class="row"><span>Chin</span><span class="price">$14</span></div>
        <div class="row"><span>Sides of face</span><span class="price">$20</span></div>
        <div class="row"><span>Bikini</span><span class="price">$27+</span></div>
      </div>
      <div>
        <h2>&nbsp;</h2>
        <div class="row"><span>Brazilian</span><span class="price">$55+</span></div>
        <div class="row"><span>Underarm</span><span class="price">$22</span></div>
        <div class="row"><span>Arms Full $40</span><span class="price">Lower $26</span></div>
        <div class="row"><span>Legs Full $62</span><span class="price">Lower $40</span></div>
        <div class="row"><span>Chest</span><span class="price">$44</span></div>
        <div class="row"><span>Back</span><span class="price">$44</span></div>
      </div>
      <div>
        <h2>Tinting</h2>
        <div class="row"><span>eyebrows</span><span class="price">$15</span></div>
        <div class="row"><span>eyelashes</span><span class="price">$20</span></div>
        <div class="row"><span>both</span><span class="price">$30</span></div>
        <p class="note">Gentle, long lasting colour that frames the eyes and brows, so you wake up polished without daily makeup.</p>
      </div>
      <div>
        <div class="service"><strong>Neck, Back &amp; Head Massage</strong><span class="dur">30 minutes $45</span></div>
        <div class="service"><strong>Aromatherapy Scalp Massage</strong><span class="dur">15 minutes $15</span></div>
        <div class="service"><strong>Foot Massage and Scrub</strong><span class="dur">15 minutes $15</span></div>
        <div class="service"><strong>Headache &amp; Migraine Relief Treatment</strong><span class="dur">30 minutes $45</span></div>
      </div>
    </div>
  </section>

  <!-- Panel 2: add ons and contact -->
  <section class="panel panel-info">
    <svg class="decor" viewBox="0 0 400 769" aria-hidden="true">
      <path d="M0 0 L40 0 C90 220 150 330 200 380 L200 400 C130 340 60 220 0 40Z" fill="var(--purple)"/>
      <path d="M400 0 L400 30 C320 200 250 320 200 400 L200 380 C250 300 320 170 360 0Z" fill="var(--purple-bright)"/>
      <path d="M400 560 C340 620 320 700 330 769 L350 769 C345 700 365 630 400 590Z" fill="var(--purple)"/>
    </svg>
    <div class="addons">
      <h2>Add Ons</h2>
      <div class="row"><span>Microdermabrasion</span><span class="price">$25</span></div>
      <div class="row"><span>Firming Lift &amp; Glow Eye Treatment</span><span class="price">$25</span></div>
      <div class="row"><span>Hot or Cold Stones</span><span class="price">$15</span></div>
      <div class="row"><span>Extended Massage</span><span class="price">$15</span></div>
      <div class="row"><span>Peppermint Scalp Massage</span><span class="price">$20</span></div>
      <div class="row"><span>Foot Scrub &amp; Massage</span><span class="price">$15</span></div>
      <div class="row"><span>Aromatherapy</span><span class="price">$10</span></div>
      <div class="row"><span>Specialty Ampoule</span><span class="price">$15</span></div>
      <div class="row"><span>Specialty Mask</span><span class="price">$15</span></div>
    </div>
    <div class="badge">
      <span class="big">%100</span>
      <span class="small">Customer<br>Satisfaction</span>
    </div>
    <div class="contact">
      <h2>• CONTACT US</h2>
      <p>COMPANY ADDRESS HERE</p>
      <p><span class="lbl">T:</span> +1 555 010 0142</p>
      <p><span class="lbl">F:</span> +1 555 010 0142</p>
      <p>hello@lumenspa.example</p>
      <div class="social"><span>SOCIAL/<em>LUMENSPA</em></span><span>FEED/<em>LUMENSPA</em></span></div>
    </div>
  </section>

  <!-- Panel 3: cover -->
  <section class="panel panel-cover">
    <svg class="decor" viewBox="0 0 400 769" aria-hidden="true">
      <path d="M0 470 C120 380 260 360 400 390 L400 410 C260 385 120 405 0 500Z" fill="var(--purple-bright)"/>
      <path d="M0 510 C120 420 260 405 400 430 L400 455 C260 430 120 450 0 540Z" fill="var(--purple)"/>
    </svg>
    <div class="photo" role="img" aria-label="Photo of a woman having makeup applied with a powder brush" style="left:0;top:450px;width:400px;height:319px;background:linear-gradient(135deg,#f6e2d6,#e8c6b0 45%,#c99a80 75%,#f4efec);clip-path:path('M0 110 C110 20 260 0 400 30 L400 319 L0 319Z')"></div>
    <div class="brand">
      <div class="name">Lumen</div>
      <div class="tag">Lash &amp; Skin Spa</div>
    </div>
    <div class="call"><span class="lbl">CALL US:</span> +1 555 010 0199</div>
  </section>

</main>
</body>
</html>
```